Business Card for Veltrano, a french tech company

Tech company
New technologies
Serious design
Dark theme

User info :
Name: Mathis CORLAVE
Position: Co-Founder & CEO
Tel: (+33) 6 58 24 90 37
Email: mathis@veltrano.io
Website: www.veltrano.io
Address: 17 rue des Tanneurs 69002 LYON

Attached is the business logo file.

```html
<!DOCTYPE html>
<html lang="en">
<head>
<meta charset="utf-8">
<title>Veltrano – Business Card</title>
<link href="https://fonts.googleapis.com/css2?family=Open+Sans:wght@400;600;700;800&display=swap" rel="stylesheet">
<style>
  :root {
    --stage: #3b3b3d;
    --card: #ffffff;
    --magenta: #c0379b;
    --purple: #7e4fa3;
    --teal: #0a6d96;
    --navy: #1c1f4e;
    --ink: #2a2a2e;
  }
  * { margin: 0; padding: 0; box-sizing: border-box; }
  html, body {
    width: 1200px; height: 689px; overflow: hidden;
    background: var(--stage);
    font-family: "Open Sans", Arial, sans-serif;
  }
  .stage {
    width: 1200px; height: 689px;
    display: flex; align-items: center; justify-content: center; gap: 40px;
  }
  .card {
    position: relative;
    width: 540px; height: 310px;
    background: var(--card);
    border-radius: 22px;
    overflow: hidden;
    box-shadow: 0 18px 40px rgba(0,0,0,.45);
  }
  .wordmark {
    font-family: "Open Sans", Arial, sans-serif;
    font-weight: 800;
    text-transform: uppercase;
    color: var(--purple);
    letter-spacing: .02em;
    line-height: 1;
  }
  .card--front { display: flex; align-items: center; justify-content: center; }
  .card--front .wordmark { font-size: 66px; }

  .card--back .wordmark {
    position: absolute; left: 34px; top: 118px; font-size: 34px;
  }
  .divider {
    position: absolute; left: 270px; top: 42px;
    width: 2px; height: 150px; background: var(--magenta);
  }
  .contact {
    position: absolute; left: 292px; top: 36px;
    color: var(--ink);
    z-index: 2;
  }
  .contact__name {
    font-size: 19px; font-weight: 700; color: var(--magenta); line-height: 1.1;
  }
  .contact__role { font-size: 12px; margin-bottom: 10px; }
  .contact__list { list-style: none; font-size: 11.5px; line-height: 1.55; }
  .contact__list li { display: flex; align-items: center; gap: 7px; }
  .contact__list svg { width: 11px; height: 11px; flex: none; }
  .contact__address { font-size: 11.5px; line-height: 1.4; margin-top: 8px; margin-left: 18px; }
  .wave { position: absolute; left: 0; top: 0; width: 540px; height: 310px; z-index: 1; }
</style>
</head>
<body>
<main class="stage">
  <section class="card card--front">
    <span class="wordmark">Veltrano</span>
  </section>

  <section class="card card--back">
    <span class="wordmark">Veltrano</span>
    <div class="divider"></div>
    <div class="contact">
      <p class="contact__name">Mathis CORLAVE</p>
      <p class="contact__role">Co-Founder &amp; CEO</p>
      <ul class="contact__list">
        <li><svg viewBox="0 0 12 12"><path fill="#c0379b" d="M2.5 1l2 2-1 1.2c.6 1.4 1.8 2.6 3.3 3.3L8 6.5l2 2-1.3 1.6C5 9.6 2.4 7 1 3.3z"/></svg>(+33) 6 58 24 90 37</li>
        <li><svg viewBox="0 0 12 12"><rect x="1" y="2.5" width="10" height="7" rx="1" fill="#c0379b"/><path d="M1.5 3l4.5 3.5L10.5 3" stroke="#fff" fill="none"/></svg>mathis@veltrano.io</li>
        <li><svg viewBox="0 0 12 12"><circle cx="6" cy="6" r="5" fill="#c0379b"/><path d="M1 6h10M6 1c-2 2.5-2 7.5 0 10M6 1c2 2.5 2 7.5 0 10" stroke="#fff" stroke-width=".8" fill="none"/></svg>www.veltrano.io</li>
      </ul>
      <p class="contact__address">17 rue des Tanneurs<br>69002 LYON</p>
    </div>
    <svg class="wave" viewBox="0 0 540 310" aria-hidden="true">
      <defs>
        <linearGradient id="bandFill" x1="0" y1="0" x2="1" y2="0">
          <stop offset="0" stop-color="#7e4fa3"/>
          <stop offset="0.55" stop-color="#8a4aa3"/>
          <stop offset="1" stop-color="#c0379b"/>
        </linearGradient>
      </defs>
      <path d="M0 302 C160 296 300 272 400 254 C460 243 505 238 540 238 L540 310 L0 310 Z" fill="url(#bandFill)"/>
      <path d="M0 296 C160 288 300 264 398 246 C455 236 495 232 525 232" stroke="#ffffff" stroke-width="4" fill="none"/>
      <path d="M0 291 C160 282 300 257 396 240 C452 230 492 226 520 226" stroke="#0a6d96" stroke-width="4" fill="none"/>
    </svg>
  </section>
</main>
</body>
</html>
```